New innovative Legal start-up looking for letterhead and business card template

Using our existing logo, colours and font we need a simple, professional, accessible (easy to read), and consistent letterhead and business card design template. Letterhead will be printed in house so heavy colour is not preferred (though some colour is acceptable). Letter sis is US Letter (21.59 cm x 27.94cm) and business card is standard size (3.5"x 2")Logo Proof sheet is attached. Logo designs can be found here https://www.stashvane.net/sh/qt4rp9zkw2vhn81/KLM7XQ3gTpbRwHsN4e2fzYdVc?dl=0

```html
<!DOCTYPE html>
<html lang="en">
<head>
<meta charset="utf-8">
<title>Northvale Stationery Set</title>
<link rel="stylesheet" href="https://fonts.googleapis.com/css2?family=Source+Sans+3:wght@300;400&display=swap">
<style>
  :root {
    --board: #3f4042;
    --paper: #ffffff;
    --navy: #1f2a4e;
    --teal: #1fa89a;
    --orange: #f07f22;
    --grey: #8c8c8c;
    --text: #7a7a7a;
    --label: #e2e2e2;
    --silver: #c9cbcd;
    --watermark: #f1f1f1;
  }
  * { margin: 0; padding: 0; box-sizing: border-box; }
  html, body { width: 1200px; height: 639px; overflow: hidden; background: var(--board); }
  body { font-family: "Source Sans 3", Arial, sans-serif; }
  .board { position: relative; width: 1200px; height: 639px; background: var(--board); }

  .piece { position: absolute; background: var(--paper); overflow: hidden; }
  .piece-label {
    position: absolute; color: var(--label); font-weight: 300;
    font-size: 9px; letter-spacing: .3px; text-align: center;
  }

  .brand { position: absolute; display: flex; align-items: center; gap: 8px; z-index: 2; }
  .brand-ring { border-radius: 50%; border: 2px solid var(--grey); flex: none; }
  .brand-name { color: var(--grey); font-weight: 300; letter-spacing: .5px; line-height: 1; }

  .letterhead { left: 85px; top: 89px; width: 361px; height: 467px; }
  .watermark-ring {
    position: absolute; left: 103px; top: 174px; width: 153px; height: 153px;
    border-radius: 50%; border: 3px solid var(--watermark);
  }

  .stripe { position: absolute; display: flex; height: 4px; }
  .stripe span { flex: 1; }
  .stripe .teal { background: var(--teal); }
  .stripe .navy { background: var(--navy); }
  .stripe .orange { background: var(--orange); }

  .contact { position: absolute; font-size: 10.5px; font-weight: 300; color: var(--text); line-height: 14px; white-space: nowrap; }
  .contact li { list-style: none; display: flex; align-items: center; gap: 5px; }
  .contact .icon { width: 9px; height: 9px; flex: none; }
  .contact .indent { padding-left: 14px; }

  .envelope-back { left: 488px; top: 119px; width: 375px; height: 177px; }
  .flap { position: absolute; left: 0; top: 0; width: 375px; height: 74px; z-index: 1; }
  .envelope-front { left: 488px; top: 344px; width: 375px; height: 177px; }

  .usb-print {
    position: absolute; left: 940px; top: 150px; width: 160px; height: 70px;
    background: var(--silver); border-radius: 6px;
  }
  .usb-cap { position: absolute; left: 0; top: 0; width: 44px; height: 70px; background: #1c1c1c; border-radius: 6px 0 0 6px; }

  .cup-wrap { left: 911px; top: 303px; width: 183px; height: 224px; border-radius: 6px; }
</style>
</head>
<body>
<main class="board">

  <section class="piece letterhead" aria-label="Letterhead">
    <div class="brand" style="left:29px;top:33px;">
      <div class="brand-ring" style="width:44px;height:44px;"></div>
      <span class="brand-name" style="font-size:22px;">NORTHVALE</span>
    </div>
    <div class="watermark-ring"></div>
    <ul class="contact" style="left:251px;top:402px;">
      <li><svg class="icon" viewBox="0 0 10 10"><path d="M5 1 L9.5 5 H8 V9 H6 V6.5 H4 V9 H2 V5 H0.5 Z" fill="var(--navy)"/></svg>418, 712 3 Ave NW</li>
      <li class="indent">Halden, AB T4K 2M6</li>
      <li><svg class="icon" viewBox="0 0 10 10"><rect x="0.5" y="2.5" width="9" height="5" rx="1" fill="var(--navy)"/></svg>info@nvlegal.ca</li>
      <li><svg class="icon" viewBox="0 0 10 10"><circle cx="5" cy="5" r="4.2" fill="none" stroke="var(--navy)" stroke-width="1.2"/><path d="M0.8 5 H9.2 M5 0.8 V9.2" stroke="var(--navy)" stroke-width="1"/></svg>www.nvlegal.ca</li>
    </ul>
    <div class="stripe" style="left:0;top:453px;width:245px;"><span class="teal"></span><span class="navy"></span><span class="orange"></span></div>
  </section>
  <p class="piece-label" style="left:85px;top:572px;width:361px;font-size:11px;">LETTER HEAD</p>

  <section class="piece envelope-back" aria-label="Envelope back">
    <svg class="flap" viewBox="0 0 375 74" preserveAspectRatio="none">
      <path d="M0 0 H375 V74 C372 58 366 49 352 49 H23 C9 49 3 58 0 74 Z" fill="var(--navy)"/>
    </svg>
    <div class="brand" style="left:143px;top:8px;gap:6px;">
      <div class="brand-ring" style="width:32px;height:32px;border-color:#fff;"></div>
      <span class="brand-name" style="font-size:17px;color:#fff;">NORTHVALE</span>
    </div>
  </section>
  <p class="piece-label" style="left:488px;top:313px;width:375px;">ENVELOPE BACK</p>

  <section class="piece envelope-front" aria-label="Envelope front">
    <div class="brand" style="left:19px;top:20px;">
      <div class="brand-ring" style="width:42px;height:42px;"></div>
      <span class="brand-name" style="font-size:21px;">NORTHVALE</span>
    </div>
    <ul class="contact" style="left:269px;top:112px;">
      <li><svg class="icon" viewBox="0 0 10 10"><path d="M5 1 L9.5 5 H8 V9 H6 V6.5 H4 V9 H2 V5 H0.5 Z" fill="var(--navy)"/></svg>418, 712 3 Ave NW</li>
      <li class="indent">Halden, AB T4K 2M6</li>
      <li><svg class="icon" viewBox="0 0 10 10"><rect x="0.5" y="2.5" width="9" height="5" rx="1" fill="var(--navy)"/></svg>info@nvlegal.ca</li>
      <li><svg class="icon" viewBox="0 0 10 10"><circle cx="5" cy="5" r="4.2" fill="none" stroke="var(--navy)" stroke-width="1.2"/><path d="M0.8 5 H9.2 M5 0.8 V9.2" stroke="var(--navy)" stroke-width="1"/></svg>www.nvlegal.ca</li>
    </ul>
    <div class="stripe" style="left:0;top:161px;width:264px;"><span class="teal"></span><span class="navy"></span><span class="orange"></span></div>
  </section>
  <p class="piece-label" style="left:488px;top:538px;width:375px;">ENVELOPE FRONT</p>

  <section class="usb-print" aria-label="USB drive print">
    <div class="usb-cap"></div>
    <div class="brand" style="left:54px;top:24px;gap:5px;">
      <div class="brand-ring" style="width:20px;height:20px;border-color:var(--navy);border-width:1.5px;"></div>
      <span class="brand-name" style="font-size:13px;color:var(--navy);">NORTHVALE</span>
    </div>
  </section>

  <section class="piece cup-wrap" aria-label="Cup print">
    <div class="brand" style="left:20px;top:100px;gap:6px;">
      <div class="brand-ring" style="width:40px;height:40px;"></div>
      <span class="brand-name" style="font-size:19px;">NORTHVALE</span>
    </div>
  </section>
  <p class="piece-label" style="left:911px;top:538px;width:183px;">CUP</p>

</main>
</body>
</html>
```